Tinselwick Flyer

Require a flyer for our pet photography business. I have uploaded a very poor attempt I have made at designing one. the size is to be DL and to be one page, but coloured on both sides. I have included the template to which the design is to fit.

Target Market(s)

Pet owners

Font styles to use
Sans Serif

Requirements
Must have
• I have included snap shots from our webdesign. The flyer design should be complimentary to the web design. Please use wording on the flyer front from the files called webscreenshots
Nice to have
• The back: a portfolio of the images on the back side with the logo and the website.
• The front: On the front side we would like a maximum of three photos (different to the ones used on the back) with the writing from the screen shots and the logo.
• check the names of the photos to be put on the flyer, I have called them back and front as appropriate.

```html
<!DOCTYPE html>
<html lang="en">
<head>
<meta charset="utf-8">
<title>Tinselwick Pet Photography – DL Flyer</title>
<link href="https://fonts.googleapis.com/css2?family=Bodoni+Moda:opsz,wght@6..96,400;6..96,500&family=Open+Sans:wght@400;600;700&display=swap" rel="stylesheet">
<style>
  :root {
    --bg: #d9d7d4;
    --black: #070707;
    --white: #ffffff;
    --paper: #f2f2f2;
    --red: #e31e25;
    --grey-text: #cfcfcf;
    --gap: #e4e4e4;
    --band-grey: #a9a9a9;
    --ink: #111111;
  }
  * { margin: 0; padding: 0; box-sizing: border-box; }
  html, body { width: 1186px; height: 1200px; overflow: hidden; background: var(--bg); }
  body { position: relative; font-family: "Open Sans", Arial, sans-serif; }

  .panel {
    position: absolute; top: 146px; width: 435px; height: 918px;
    background: var(--black); overflow: hidden;
    box-shadow: 0 6px 14px rgba(0,0,0,.25);
  }
  .panel--front { left: 118px; }
  .panel--back { left: 633px; background: var(--gap); }

  .abs { position: absolute; }
  .centered { left: 0; width: 100%; text-align: center; white-space: nowrap; }

  /* front */
  .pet-photo-hero {
    left: 42px; top: 190px; width: 328px; height: 545px;
    background: radial-gradient(ellipse 50% 50% at 50% 50%, #ddd5cb 0%, #a99e92 40%, #3c3632 75%, rgba(7,7,7,0) 100%);
  }
  .front-curve { left: 0; top: 0; width: 435px; height: 330px; }
  .brand-mark {
    left: 176px; top: 12px; width: 82px; height: 82px;
    border: 3px solid var(--black); border-radius: 50%;
  }
  .brand-name {
    top: 100px; font-family: "Bodoni Moda", "Times New Roman", serif;
    font-size: 34px; line-height: 38px; font-weight: 500;
    color: var(--red); letter-spacing: 1px; text-transform: uppercase;
    font-optical-sizing: auto;
  }
  .brand-sub {
    top: 134px; font-size: 14px; line-height: 16px; font-weight: 700;
    color: var(--ink); letter-spacing: 3px; text-transform: uppercase;
  }
  .badge {
    left: 290px; top: 520px; width: 116px; height: 116px; border-radius: 50%;
    background: var(--white); border: 3px solid #3a3a3a;
  }
  .headline {
    font-family: "Bodoni Moda", "Times New Roman", serif; color: var(--white);
    font-weight: 400; font-optical-sizing: auto; text-transform: uppercase;
  }
  .front-headline { top: 662px; font-size: 27px; line-height: 36px; letter-spacing: 0; }
  .tagline-red { color: var(--red); font-size: 18px; line-height: 24px; }
  .front-available { top: 743px; }
  .services-grey { top: 780px; color: var(--grey-text); font-size: 18px; line-height: 24px; letter-spacing: .3px; }
  .call-band {
    left: 0; top: 820px; width: 100%; height: 48px; background: var(--red);
    color: var(--white); font-size: 24px; line-height: 48px; text-align: center; white-space: nowrap;
  }
  .call-band svg { width: 20px; height: 20px; vertical-align: -2px; margin: 0 4px 0 6px; }
  .website { top: 879px; color: var(--white); font-size: 14.5px; line-height: 20px; letter-spacing: .2px; }

  /* back */
  .photo { position: absolute; }
  .photo--horse { left: 0; top: 0; width: 435px; height: 167px;
    background: linear-gradient(100deg, #5a2e1c 0%, #7b4428 45%, #c69a6c 70%, #e9dfd2 100%); }
  .photo--fluffy-dog { left: 0; top: 176px; width: 139px; height: 155px;
    background: radial-gradient(circle at 50% 55%, #d9ccb7 0%, #8a7560 40%, #3f2f24 100%); }
  .photo--owner { left: 149px; top: 176px; width: 286px; height: 155px;
    background: linear-gradient(90deg, #e6dccd 0%, #d9cbb8 55%, #a88a6c 100%); }
  .photo--shar-pei { left: 0; top: 338px; width: 139px; height: 154px;
    background: radial-gradient(circle at 45% 45%, #d4a777 0%, #8c6a4d 45%, #2f2a28 100%); }
  .photo--poodle { left: 149px; top: 338px; width: 144px; height: 154px;
    background: radial-gradient(circle at 50% 50%, #fbf3f1 0%, #f3c9c4 55%, #e9b3ad 100%); }
  .photo--cat { left: 296px; top: 338px; width: 139px; height: 154px;
    background: linear-gradient(135deg, #d8d4cd 0%, #8a7a63 50%, #4d4030 100%); }
  .back-body { left: 0; top: 502px; width: 100%; height: 416px; background: var(--black); }
  .back-headline { top: 528px; font-size: 38px; line-height: 44px; }
  .back-services { top: 577px; color: var(--red); font-size: 21px; line-height: 28px; }
  .body-copy { color: var(--white); font-size: 15px; line-height: 20px; padding: 0 26px; white-space: normal; }
  .back-copy-1 { top: 613px; }
  .pill {
    left: 122px; top: 690px; width: 188px; height: 29px; border-radius: 15px;
    background: var(--red); color: var(--white); font-size: 17px; line-height: 29px; text-align: center;
  }
  .back-copy-2 { top: 728px; }
  .back-available { top: 782px; }
</style>
</head>
<body>

<section class="panel panel--front">
  <div class="abs pet-photo-hero" role="img" aria-label="Fluffy long-haired tabby cat photographed from below, paws raised, on black"></div>
  <svg class="abs front-curve" viewBox="0 0 435 330" aria-hidden="true">
    <path d="M0 0 L435 0 L435 160 C250 170 80 215 0 292 Z" fill="var(--paper)"/>
    <path d="M0 307 C80 230 250 185 435 176" fill="none" stroke="var(--band-grey)" stroke-width="7"/>
  </svg>
  <div class="abs brand-mark" aria-hidden="true"></div>
  <div class="abs centered brand-name">Tinselwick</div>
  <div class="abs centered brand-sub">Pet Photography</div>
  <div class="abs badge" aria-hidden="true"></div>

  <h1 class="abs centered headline front-headline">Fun Quirky &amp; Beautiful<br>Pet Photography</h1>
  <p class="abs centered tagline-red front-available">Now available in Mackay</p>
  <p class="abs centered services-grey">In Studio | On Location | At Home</p>

  <div class="abs call-band">Call Marla at:<svg viewBox="0 0 24 24" aria-hidden="true"><circle cx="12" cy="12" r="10.5" fill="none" stroke="#fff" stroke-width="2"/><path d="M8.3 6.8c.5-.4 1.1-.3 1.4.2l1 1.7c.3.5.2 1-.2 1.3l-.7.6c.6 1.4 1.7 2.6 3.1 3.3l.6-.7c.4-.4.9-.5 1.3-.2l1.7 1c.5.3.6.9.2 1.4l-.8.9c-.6.6-1.6.8-2.6.3-2.6-1.2-4.5-3.2-5.700-5.8-.4-1-.2-1.9.4-2.5z" fill="#fff"/></svg>0400 555 218</div>
  <p class="abs centered website">www.tinselwickpetphotography.com</p>
</section>

<section class="panel panel--back">
  <div class="photo photo--horse" role="img" aria-label="Woman with long hair resting her face against a brown horse at sunset"></div>
  <div class="photo photo--fluffy-dog" role="img" aria-label="Small fluffy cream dog sitting on a dark studio backdrop"></div>
  <div class="photo photo--owner" role="img" aria-label="Smiling owner seated in a leather chair hugging a dark dog"></div>
  <div class="photo photo--shar-pei" role="img" aria-label="Shar-pei dog with red collar on grey backdrop"></div>
  <div class="photo photo--poodle" role="img" aria-label="White poodle with pink ears and flower collar on pink backdrop"></div>
  <div class="photo photo--cat" role="img" aria-label="Calico cat sitting in a wicker chair"></div>

  <div class="abs back-body"></div>
  <h2 class="abs centered headline back-headline">Be at Ease</h2>
  <p class="abs centered back-services">In Studio | On Location | At Home</p>
  <p class="abs centered body-copy back-copy-1">All session are available to ensure you and your pet are comforbole</p>
  <div class="abs pill">You Get It All!</div>
  <p class="abs centered body-copy back-copy-2">Beautifully printed photographs on art paper along with the digital files.</p>
  <p class="abs centered tagline-red back-available">Now available in Mackay</p>

  <div class="abs call-band">Call Marla at:<svg viewBox="0 0 24 24" aria-hidden="true"><circle cx="12" cy="12" r="10.5" fill="none" stroke="#fff" stroke-width="2"/><path d="M8.3 6.8c.5-.4 1.1-.3 1.4.2l1 1.7c.3.5.2 1-.2 1.3l-.7.6c.6 1.4 1.7 2.6 3.1 3.3l.6-.7c.4-.4.9-.5 1.3-.2l1.7 1c.5.3.6.9.2 1.4l-.8.9c-.6.6-1.6.8-2.6.3-2.6-1.2-4.5-3.2-5.7-5.8-.4-1-.2-1.9.4-2.5z" fill="#fff"/></svg>0400 555 218</div>
  <p class="abs centered website">www.tinselwickpetphotography.com</p>
</section>

</body>
</html>
```